bizcards, stationary, envelopes, powerpoint template, invoice template, polo shirts, email template
ms word templates of stationary also please
bizcards, stationary, envelopes,  powerpoint template, invoice template, polo shirts, email template - Aviation
Creative Brief
Professional
Samuel K Orlowski
Founder
The Halvern Tower 482 Tamsin Ridge Rd. Suite 210 Westlake, OH 44718
sorlowski@meridowair.example
www.meridowair.example
Air Carrier #4RXB519T
Only use the colors and font of our logo. Our tag line "THE SPEED IS YOURS" can be used in a creative way of your thoughts.
wide ope, maybe a Skyvalent Jet watermark, the tag line, the tag line & logo, etc.

```html
<!DOCTYPE html>
<html lang="en">
<head>
<meta charset="utf-8">
<title>Meridow Air Charter – Business Card</title>
<link rel="stylesheet" href="https://fonts.googleapis.com/css2?family=Open+Sans:wght@400;600;700&display=swap">
<style>
  :root {
    --backdrop: #ecebe8;
    --card-white: #ffffff;
    --brand-green: #8cc63f;
    --brand-green-deep: #5f9a22;
    --swoosh-grey: #7a7a7a;
    --name-grey: #555759;
    --muted-grey: #8a8a8a;
    --text-on-green: #ffffff;
  }
  html, body {
    margin: 0;
    padding: 0;
    width: 1200px;
    height: 935px;
    overflow: hidden;
    background: var(--backdrop);
    font-family: "Open Sans", Arial, sans-serif;
  }
  .business-card {
    position: absolute;
    left: 100px;
    top: 180px;
    width: 1000px;
    height: 575px;
    border-radius: 34px;
    overflow: hidden;
    background: var(--card-white);
    box-shadow: 0 10px 30px rgba(0,0,0,0.18);
  }
  .card-shapes {
    position: absolute;
    inset: 0;
  }
  .holder {
    position: absolute;
    right: 52px;
    top: 34px;
    text-align: right;
  }
  .holder-name {
    margin: 0;
    font-size: 34px;
    font-weight: 700;
    color: var(--brand-green);
    line-height: 1.1;
  }
  .holder-title {
    margin: 4px 0 0;
    font-size: 17px;
    font-weight: 400;
    color: var(--muted-grey);
  }
  .company-name {
    position: absolute;
    left: 96px;
    top: 196px;
    margin: 0;
    font-size: 62px;
    font-weight: 600;
    letter-spacing: 1px;
    color: var(--name-grey);
    line-height: 1;
  }
  .contact {
    position: absolute;
    left: 60px;
    right: 30px;
    top: 392px;
    text-align: center;
    color: var(--text-on-green);
    font-size: 20px;
    font-style: normal;
    line-height: 1.5;
  }
  .contact p { margin: 0; }
  .contact .label { font-weight: 700; }
  .contact .gap { display: inline-block; width: 14px; }
</style>
</head>
<body>
  <article class="business-card">
    <svg class="card-shapes" viewBox="0 0 1000 575" preserveAspectRatio="none" aria-hidden="true">
      <defs>
        <linearGradient id="greenPanel" x1="0" y1="0" x2="0.3" y2="1">
          <stop offset="0" stop-color="#8cc63f"/>
          <stop offset="1" stop-color="#5f9a22"/>
        </linearGradient>
      </defs>
      <path class="swoosh" d="M0 360 C 220 300, 420 360, 640 330 C 800 308, 900 280, 1000 262 L1000 575 L0 575 Z" fill="#7a7a7a"/>
      <path class="green-panel" d="M0 378 C 230 330, 430 380, 650 350 C 810 330, 910 300, 1000 290 L1000 575 L0 575 Z" fill="url(#greenPanel)"/>
    </svg>

    <header class="holder">
      <h1 class="holder-name">Samuel K Orlowski</h1>
      <p class="holder-title">Founder</p>
    </header>

    <p class="company-name">Meridow Air</p>

    <address class="contact">
      <p>The Halvern Tower 482 Tamsin Ridge Rd. Suite 210 Westlake, OH 44718</p>
      <p><span class="label">Phone :</span> 440-555-0147<span class="gap"></span><span class="label">Cell :</span> 216-555-0182 <span class="label">Fax :</span> 440-555-0139</p>
      <p><span class="label">License No :</span> Air Carrier #4RXB519T</p>
      <p><span class="label">Email :</span> sorlowski@meridowair.example<span class="gap"></span><span class="label">Web :</span> www.meridowair.example</p>
    </address>
  </article>
</body>
</html>
```